Book Marketing Site for authors needs redesign

I need a site redesign for the site www.quorvanta.com I would like to have it designed/created in Wordpress so that I can change/edit the text as necessary. Ideally, we can simplify the site so that Wordpress updates do not impact the functionality of the site.

I want to continue to use the Quorvant logo, so I would like the site to work the existing logo. I am also planning to add the tag line Book Marketing Simplified so please incorporate the tag line with the logo and the site.

Initially, I would like to see the page design template and then once that is approved, you to program the site. Wherever, I have indicated that we would capture email addresses; I would like to set it up so that the names are captured in my Mellow Relay account.

Below are the elements that will need to be part of the site:
_______

Elements that should be above the fold:

• Chirply, Facemuro, Vexor+ and Pindle up buttons with the copy “Connect with Miriam”
o
• The copy “Sign up for our free newsletter and receive our list of Top Chirply Tips for Authors Free!” with a box to enter email address. The button should say “Go” not "Submit".
• A space/box for a short, 10-15 word testimonials. The testimonials will need to change from page to page.

Nav Bar/sub nav bars

Services
Packages Speaking Testimonials
FAQ
-
About Us
Speaking
-
Resources
-
Our clients
Testimonials
-
Blog
-
Contact Us

Home page
• Should have the following copy:
High Impact Book Marketing for Authors

QuorVant Marketing is book marketing service that that provides authors with an effective,
affordable approach to marketing their book.

We provide marketing coaching and consulting services that accelerate book sales, target your ideal reader and develop a community of fans that will promote your book for you.

Using high impact, low cost marketing strategies, we will develop a book marketing strategy that achieves your goals and accommodates your budget

Do you
• Want to be a best selling author, but need someone to show you the way

• Wonder what is the secret to achieving high book sales?

• Worry that you aren’t doing the right things to ensure that your book is a success?

• Need someone to help keep your spirits up and maintain momentum?

• Please put the following copy in a box at the bottom of the copy.
o Are you ready for results? Call now for a free consultation 318-546-0821

Services Page
• Copy to come

Packages Page

FAQ Page
• Same as existing site

About page
• Same as existing site

Speaking Page

Speaking

If you’re looking to create an exceptional program that your attendees won’t be able to stop talking about, you have found it!

Miriam Tolberg, a leader in book marketing, has ability to make sophisticated internet concepts easy and accessible, and the unique ability to not only to inform, but also to inspire. Her presentations leave participants with tangible, actionable ideas proven to increase book sales.

Miriam's talks combine practical step-by-step instructions, real-life examples with plenty of humor. Call 318-546-0821 to book her now!

Miriam’s most popular talks:

• Unlocking the Power of Pagewell
• How to Simplify Social Media
• The Ideal Author Website
• Orvex: What You Need to Know to Succeed

Resources page
• Same as existing site

Clients
• Same as existing site

Testimonials
• I would like to be able to put a image of book cover next to the testimonial on this page.

Blog page
• Please add the following elements:
• A way to sign up for the blog via RSS
o Each blog article should have a way to Facemuro like, Chirp, V+, Plink and Wanderclip the article

Contact us page
• Same as existing site

Site Map
• Please make sure to include a site map.

Chirply and Facemuro headers
• Please provide both with consistent branding.

Target Market(s)

Clients are both traditionally and indie published authors trying to be the next P.J. Harwick!

Industry/Entity Type

Marketing

Requirements
Must have
• Elements that should be above the fold:

o

```html
<!DOCTYPE html>
<html lang="en">
<head>
<meta charset="utf-8">
<title>QuorVant Marketing – Book Marketing Simplified</title>
<link rel="stylesheet" href="https://fonts.googleapis.com/css2?family=Arimo:wght@400;700&family=Krona+One&family=Michroma&family=Oswald:wght@500&family=PT+Sans:wght@700&display=swap">
<style>
  :root {
    --navy: #004a93;
    --blue: #1e5fae;
    --sky: #5e8fc4;
    --green: #78bf3f;
    --line-green: #9ccb74;
    --panel: #9dbad8;
    --field: #b6cde6;
    --ink: #333333;
    --grey: #666666;
    --quote: #6a6a6a;
    --white: #ffffff;
  }
  * { box-sizing: border-box; margin: 0; padding: 0; }
  html, body { width: 1043px; height: 1200px; overflow: hidden; background: var(--white); }
  body { position: relative; font-family: "Arimo", Arial, sans-serif; color: var(--ink); }
  .abs { position: absolute; }

  /* header */
  .brand { left: 26px; top: 44px; display: flex; align-items: center; gap: 10px; }
  .brand-mark { width: 22px; height: 22px; background: var(--sky); }
  .brand-name { font-family: "Michroma", sans-serif; font-size: 17px; letter-spacing: 7px; color: var(--navy); }
  .tagline { left: 0; width: 1043px; top: 42px; text-align: center; font-family: "Michroma", sans-serif; font-size: 22px; color: var(--blue); }
  .tagline span { color: var(--green); }
  .connect { left: 848px; top: 40px; width: 180px; text-align: center; font-family: "PT Sans", sans-serif; font-weight: 700; font-size: 14px; color: var(--sky); }
  .socials { left: 858px; top: 62px; display: flex; gap: 10px; list-style: none; }
  .socials li { width: 32px; text-align: center; font-size: 7px; line-height: 9px; color: var(--sky); }
  .socials .dot { display: block; width: 30px; height: 30px; margin: 0 auto 2px; border-radius: 50%; background: #8eb3da; }

  .rule-green { left: 0; width: 1043px; height: 3px; background: var(--line-green); }
  .nav { left: 0; top: 111px; width: 1043px; height: 43px; background: var(--navy); list-style: none; }
  .nav li { position: absolute; top: 13px; font-family: "Michroma", sans-serif; font-size: 12.5px; color: var(--white); }

  .hero { left: 0; top: 154px; width: 1043px; height: 306px;
    background: linear-gradient(180deg, #b9d08c 0%, #a9c578 35%, #c6a16a 62%, #a7804e 80%, #e9ecde 100%); }
  .hero-shade { left: 60px; top: 460px; width: 923px; height: 12px; background: radial-gradient(ellipse at top, rgba(0,0,0,.12), rgba(0,0,0,0) 70%); }

  /* main copy */
  .headline { left: 27px; top: 497px; font-family: "Krona One", sans-serif; font-size: 21px; color: var(--navy); }
  .headline span { color: var(--grey); }
  .intro { left: 27px; top: 540px; width: 610px; font-size: 14.5px; line-height: 18px; }
  .intro p { margin-bottom: 17px; }
  .section-title { font-family: "Krona One", sans-serif; font-size: 21px; color: var(--navy); }
  .do-you { left: 27px; top: 725px; }
  .checklist { left: 44px; top: 766px; width: 520px; list-style: none; font-size: 14.5px; line-height: 18px; }
  .checklist li { position: relative; padding-left: 25px; margin-bottom: 9px; }
  .checklist svg { position: absolute; left: 0; top: 1px; }
  .cta { left: 27px; top: 922px; font-family: "PT Sans", sans-serif; font-weight: 700; font-size: 18.5px; color: var(--grey); }
  .phone { left: 27px; top: 955px; display: flex; align-items: center; gap: 9px; font-family: "Oswald", sans-serif; font-weight: 500; font-size: 38px; color: var(--grey); }

  /* newsletter */
  .newsletter { left: 688px; top: 499px; width: 329px; height: 203px; border-radius: 8px; background: var(--panel); color: var(--white); }
  .newsletter h2 { position: absolute; left: 32px; top: 20px; font-family: "Arimo", sans-serif; font-weight: 400; font-size: 25px; }
  .newsletter p { position: absolute; left: 28px; top: 58px; width: 285px; font-size: 12.5px; line-height: 15px; }
  .newsletter .field { position: absolute; left: 27px; top: 100px; width: 266px; height: 35px; border: 1px solid #8fb0d3; border-radius: 9px; background: var(--field); }
  .newsletter .go { position: absolute; left: 27px; top: 148px; width: 77px; height: 33px; border: 0; border-radius: 5px; background: linear-gradient(#5a8fcb, #3f6fae); color: var(--white); font-family: "PT Sans", sans-serif; font-weight: 700; font-size: 13px; }

  /* testimonials */
  .testimonials-title { left: 690px; top: 725px; color: var(--sky); }
  .quote { left: 688px; width: 330px; font-size: 12px; line-height: 14px; color: var(--quote); }
  .quote cite { display: block; margin-top: 2px; font-style: normal; font-family: "PT Sans", sans-serif; font-weight: 700; font-size: 13.5px; color: var(--sky); }

  /* footer */
  .footer-band { left: 0; top: 1090px; width: 1043px; height: 11px; background: var(--blue); }
  .footer-nav { left: 0; top: 1124px; width: 1043px; text-align: center; font-size: 13px; color: var(--ink); }
  .copyright { left: 0; top: 1149px; width: 1043px; text-align: center; font-size: 11px; color: var(--grey); }
</style>
</head>
<body>
  <header>
    <div class="abs brand"><span class="brand-mark"></span><span class="brand-name">QUORVANT</span></div>
    <div class="abs tagline">Book Marketing <span>Simplified</span></div>
    <div class="abs connect">CONNECT WITH MIRIAM</div>
    <ul class="abs socials">
      <li><span class="dot"></span>Chirply</li>
      <li><span class="dot"></span>Facemuro</li>
      <li><span class="dot"></span>Vexor+</li>
      <li><span class="dot"></span>Pindle up</li>
    </ul>
  </header>

  <div class="abs rule-green" style="top:106px"></div>
  <ul class="abs nav">
    <li style="left:28px">SERVICES</li>
    <li style="left:184px">ABOUT US</li>
    <li style="left:351px">RESOURCES</li>
    <li style="left:535px">OUR CLIENTS</li>
    <li style="left:725px">BLOG</li>
    <li style="left:857px">CONTACT US</li>
  </ul>

  <div class="abs hero" role="img" aria-label="Close-up photograph of an open book with gilded page edges on a soft green background"></div>
  <div class="abs hero-shade"></div>

  <main>
    <h1 class="abs headline">High Impact <span>Book Marketing</span> for Authors</h1>
    <div class="abs intro">
      <p>QuorVant Marketing is book marketing service that that provides authors with an effective, affordable approach to marketing their book.</p>
      <p>We provide marketing coaching and consulting services that accelerate book sales, target your ideal reader and develop a community of fans that will promote your book for you.</p>
      <p>Using high impact, low cost marketing strategies, we will develop a book marketing strategy that achieves your goals and accommodates your budget</p>
    </div>

    <h2 class="abs section-title do-you">Do you</h2>
    <ul class="abs checklist">
      <li><svg width="16" height="16" viewBox="0 0 16 16"><circle cx="7" cy="9" r="6" fill="#3a9a2a"/><path d="M4 9l3 3 8-10" stroke="#1c1c1c" stroke-width="2.4" fill="none"/></svg>Want to be a best selling author, but need someone to show you the way</li>
      <li><svg width="16" height="16" viewBox="0 0 16 16"><circle cx="7" cy="9" r="6" fill="#3a9a2a"/><path d="M4 9l3 3 8-10" stroke="#1c1c1c" stroke-width="2.4" fill="none"/></svg>Wonder what is the secret to achieving high book sales?</li>
      <li><svg width="16" height="16" viewBox="0 0 16 16"><circle cx="7" cy="9" r="6" fill="#3a9a2a"/><path d="M4 9l3 3 8-10" stroke="#1c1c1c" stroke-width="2.4" fill="none"/></svg>Worry that you aren’t doing the right things to ensure that your book<br>is a success?</li>
      <li><svg width="16" height="16" viewBox="0 0 16 16"><circle cx="7" cy="9" r="6" fill="#3a9a2a"/><path d="M4 9l3 3 8-10" stroke="#1c1c1c" stroke-width="2.4" fill="none"/></svg>Need someone to help keep your spirits up and maintain momentum?</li>
    </ul>

    <p class="abs cta">Are you ready for results? Call now for a free consultation</p>
    <div class="abs phone">
      <svg width="36" height="36" viewBox="0 0 36 36"><circle cx="18" cy="18" r="16.5" fill="none" stroke="#666" stroke-width="2"/><path d="M12 9c2-1 3 0 4 3s0 3-1 4c1 3 3 5 5 6 1-1 2-2 4-1s4 2 3 4-3 3-5 2C15 25 10 19 10 13c0-2 1-3 2-4z" fill="#666"/></svg>
      318-546-0821
    </div>
  </main>

  <aside>
    <form class="abs newsletter">
      <h2>Our Newsletter</h2>
      <p>Sign up for our free newsletter and receive our list of Top Chirply Tips for Authors Free!</p>
      <div class="field"></div>
      <button class="go" type="button">GO</button>
    </form>

    <h2 class="abs section-title testimonials-title">Testimonials</h2>
    <blockquote class="abs quote" style="top:771px">"I would not be where I am, were it not for Miriam's marketing advice."<cite>- Dana Hollick</cite></blockquote>
    <blockquote class="abs quote" style="top:844px">"We provide marketing coaching and consulting services that accelerate book sales, targetyour ideal.".<cite>- Brent Callow</cite></blockquote>
    <blockquote class="abs quote" style="top:910px">"A space/box for a short, 10-15 word testimonials. The testimonials will need to change from page to page"<cite>- Marla Fennick</cite></blockquote>
    <blockquote class="abs quote" style="top:988px">"I would not be where I am, were it not for Miriam's marketing advice."<cite>- Orla Vantrees</cite></blockquote>
  </aside>

  <footer>
    <div class="abs rule-green" style="top:1084px;height:4px"></div>
    <div class="abs footer-band"></div>
    <nav class="abs footer-nav">SERVICES · ABOUT US · RESOURCES · OUR CLIENTS · BLOG · CONTACT US</nav>
    <p class="abs copyright">Copyright © 2005 - 2013 QuorVant Consulting. All rights reserved.</p>
  </footer>
</body>
</html>
```